Pelican Litigation Funding Letterhead & Document Template

We need a letter head designed for our fund. Our fund works with law firms and investors across the globe. We need a a cover letter template as well as a document template for subsequent pages. Blue and white color scheme is preferred. This is our predecessor's website: https://www.pelicanvq.com/index.html. Please see our logo attached. The logo color code is #19478d. Font is Gotham-Medium.
Target Market(s)
Sophisticated investors and law firms
Font styles to use
Sans Serif
Colors
0255a3

```html
<!DOCTYPE html>
<html lang="en">
<head>
<meta charset="utf-8">
<title>Pelican Litigation Funding – Stationery</title>
<link href="https://fonts.googleapis.com/css2?family=Montserrat:wght@500&family=Open+Sans:wght@400&family=Roboto:wght@400&display=swap" rel="stylesheet">
<style>
  :root {
    --brand-blue: #385e98;
    --brand-blue-deep: #19478d;
    --paper: #fafafa;
    --backdrop: #e0e0e0;
    --ink: #555555;
    --signature-tone: #ececec;
  }
  * { margin: 0; padding: 0; box-sizing: border-box; }
  html, body { width: 1200px; height: 800px; overflow: hidden; }
  body {
    background: var(--backdrop);
    position: relative;
    font-family: "Open Sans", sans-serif;
  }
  .cover-page {
    position: absolute;
    left: 164px; top: 111px;
    width: 408px; height: 574px;
    background: var(--brand-blue);
    display: flex; align-items: center; justify-content: center;
  }
  .cover-name {
    font-family: "Montserrat", sans-serif;
    font-weight: 500;
    color: #ffffff;
    font-size: 22px;
    letter-spacing: 0.5px;
    text-align: center;
    line-height: 1.3;
  }
  .letter-page {
    position: absolute;
    left: 613px; top: 110px;
    width: 408px; height: 574px;
    background: var(--paper);
  }
  .letter-header {
    position: absolute;
    top: 76px; left: 0; width: 100%;
    text-align: center;
  }
  .letter-name {
    font-family: "Montserrat", sans-serif;
    font-weight: 500;
    color: var(--brand-blue-deep);
    font-size: 11.5px;
    letter-spacing: 0.2px;
  }
  .letter-body {
    position: absolute;
    left: 37px; top: 148px;
    width: 335px;
    color: var(--ink);
    font-size: 7.6px;
    line-height: 11.1px;
    text-align: justify;
  }
  .letter-body p { margin-bottom: 11.1px; }
  .letter-body .salutation { margin-bottom: 11.1px; }
  .signature-area {
    position: absolute;
    left: 37px; top: 437px;
    width: 50px; height: 47px;
    background: var(--signature-tone);
    border-radius: 4px;
  }
  .contact-list {
    position: absolute;
    left: 37px; top: 502px;
    font-family: "Roboto", sans-serif;
    font-size: 7.8px;
    line-height: 9.8px;
    color: var(--ink);
    list-style: none;
  }
  .contact-list li { display: flex; align-items: center; gap: 3px; }
  .contact-list svg { width: 6.5px; height: 6.5px; fill: var(--brand-blue); }
  .office-address {
    position: absolute;
    left: 266px; top: 507px;
    font-family: "Roboto", sans-serif;
    font-style: normal;
    font-size: 7.8px;
    line-height: 9.4px;
    color: var(--ink);
  }
</style>
</head>
<body>
  <section class="cover-page">
    <div class="cover-name">Pelican Litigation<br>Funding</div>
  </section>

  <section class="letter-page">
    <header class="letter-header">
      <div class="letter-name">PELICAN LITIGATION FUNDING</div>
    </header>

    <div class="letter-body">
      <p class="salutation">Dear customer,</p>
      <p>Lorem ipsum dolor sit amet, consectetur adipisicing elit, sed do eiusmod tempor incididunt ut labore et dolore magna aliqua. Ut enim ad minim veniam, quis nostrud exercitation ullamco laboris nisi ut aliquip ex ea commodo consequat. Duis aute irure dolor in reprehenderit in voluptate velit esse cillum dolore eu fugiat nulla pariatur. Excepteur sint occaecat cupidatat non proident, sunt in culpa qui officia deserunt mollit anim id est laborum.</p>
      <p>Lorem ipsum dolor sit amet, consectetur adipisicing elit, sed do eiusmod tempor incididunt ut labore et dolore magna aliqua. Ut enim ad minim veniam, quis nostrud exercitation ullamco laboris nisi ut aliquip ex ea commodo consequat. Duis aute irure dolor in reprehenderit in voluptate velit esse cillum dolore eu fugiat nulla pariatur. Excepteur sint occaecat cupidatat non proident, sunt in culpa qui officia deserunt mollit anim id est laborum.</p>
      <p>Lorem ipsum dolor sit amet, consectetur adipisicing elit, sed do eiusmod tempor incididunt ut labore et dolore magna aliqua. Ut enim ad minim veniam, quis nostrud exercitation ullamco laboris nisi ut aliquip ex ea commodo consequat. Duis aute irure dolor in reprehenderit in voluptate velit esse cillum dolore eu fugiat nulla pariatur. Excepteur sint occaecat cupidatat non proident, sunt in culpa qui officia deserunt mollit anim id est laborum.</p>
      <p>Lorem ipsum dolor sit amet, consectetur adipisicing elit, sed do eiusmod tempor incididunt ut labore et dolore magna aliqua. Ut enim ad minim veniam, quis nostrud exercitation ullamco laboris nisi ut aliquip ex ea commodo consequat. Duis aute irure dolor in reprehenderit.</p>
      <p>Yours Sincerely,</p>
    </div>

    <div class="signature-area" role="img" aria-label="Handwritten signature of the sender"></div>

    <ul class="contact-list">
      <li><svg viewBox="0 0 10 10"><path d="M1 3c0-1 1-2 4-2s4 1 4 2v1H7V3H3v1H1zM2 5h6l1 4H1z"/></svg>(555) 014-7200</li>
      <li><svg viewBox="0 0 10 10"><path d="M3 1h4v2H3zM1 3h8v4H7v2H3V7H1zM4 6v2h2V6z"/></svg>(555) 014-7300</li>
      <li><svg viewBox="0 0 10 10"><path d="M1 2h8v6H1zM1.5 2.5 5 5.5l3.5-3"/></svg>info@pelicanvq.com</li>
      <li><svg viewBox="0 0 10 10"><circle cx="5" cy="5" r="4.5"/></svg>www.pelicanvq.com</li>
    </ul>

    <address class="office-address">
      Harbor Point - Penthouse Floor<br>
      4810 Meridian Avenue, Suite<br>
      1200 Houston, Texas 77000
    </address>
  </section>
</body>
</html>
```